B2B EDM Banner Design- Specialist Tech Company

We need a new top-of-email banner for our EDM campaigns for Varnel Brix (www.varnelbrix-example.com
). This banner will sit at the top of every email and must immediately signal the brand, look modern and professional, and be visually aligned with the tech/IT audience.
Size of the banner: Around 728x90 - it must fit at the top of an email blast.
Purpose of the Banner
Establish a strong, recognizable brand identity across all Varnel Brix EDMs
visually consistent with existing banners created for other brands (see reference examples provided)
Communicate Varnel Brix’s value proposition at a glance
Brand Name
Varnel Brix
Tagline (must appear in the banner)
“11,322 whitepapers from 726 companies”
Design Requirements
Style & Tone
Modern, clean, and professional
Tech-centric look and feel
High-quality, sleek, and corporate
Eye-catching but not cluttered
Should feel premium and authoritative
Layout & Composition
Full-width banner for email header
Horizontal orientation similar to the Plomtar and Quindle Staff Archive examples
Include space for the brand name/logo prominently on the left or centered
Integrate the tagline in a readable, secondary position
Optional: a subtle background texture or tech-related abstract pattern (circuitry, network nodes, gradient, etc.)
No busy imagery—should feel clean and trustworthy
Color Palette
Use colors consistent with Varnel Brix branding from www.varnelbrix-example.com
Blues, greys, blacks, and tech-style gradients preferred
Should feel consistent with a B2B IT audience
Typography
Clean, sans-serif fonts (professional/tech-aligned)
Brand name should be bold and prominent
Tagline should be smaller, but still readable on desktop and mobile
Imagery (if used)
Abstract tech shapes, network visuals, geometric patterns, or gradient overlays
Avoid photography of people
Keep imagery subtle so text remains legible
Call-to-Action Button (optional)
None required in this banner (unlike the HR examples)
Banner should remain a pure brand header
Deliverables
Final banner in PNG and JPG formats
2–3 design variations (if possible) for A/B testing
Dimensions optimized for EDM: ~600–700px wide (standard email width), proportionate height

```html
<!DOCTYPE html>
<html lang="en">
<head>
<meta charset="utf-8">
<title>Varnel Brix – Email Header Banner</title>
<link rel="stylesheet" href="https://fonts.googleapis.com/css2?family=Arimo:wght@700&family=Montserrat:wght@800&display=swap">
<style>
  :root {
    --bg-deep: #0d0b26;
    --bg-mid: #1c1550;
    --bg-violet: #35217a;
    --globe-glow: #d77ae8;
    --globe-violet: #7a3fd0;
    --brand-blue: #1a9fe0;
    --text-white: #ffffff;
  }
  html, body {
    margin: 0;
    padding: 0;
    width: 1200px;
    height: 150px;
    overflow: hidden;
    background: var(--bg-deep);
  }
  .banner {
    position: relative;
    width: 1200px;
    height: 150px;
    overflow: hidden;
    background: linear-gradient(90deg, var(--bg-violet) 0%, var(--bg-mid) 40%, var(--bg-deep) 100%);
  }
  .globe-art {
    position: absolute;
    left: 0;
    top: 0;
    width: 260px;
    height: 150px;
  }
  .brand {
    position: absolute;
    left: 241px;
    top: 48px;
    display: flex;
    align-items: center;
    gap: 16px;
  }
  .brand-mark {
    width: 54px;
    height: 54px;
    border-radius: 50%;
    background: var(--brand-blue);
  }
  .brand-name {
    font-family: "Montserrat", sans-serif;
    font-weight: 800;
    font-size: 31px;
    letter-spacing: 0.5px;
    color: var(--text-white);
    text-transform: uppercase;
    white-space: nowrap;
  }
  .tagline {
    position: absolute;
    left: 639px;
    top: 56px;
    margin: 0;
    font-family: "Arimo", sans-serif;
    font-weight: 700;
    font-size: 25px;
    line-height: 30px;
    color: var(--text-white);
    white-space: nowrap;
  }
</style>
</head>
<body>
  <header class="banner">
    <svg class="globe-art" viewBox="0 0 260 150" role="img" aria-label="Abstract glowing globe of pink and violet dots linked by network lines">
      <defs>
        <radialGradient id="globeGlow" cx="0.62" cy="0.05" r="0.95">
          <stop offset="0" stop-color="var(--globe-glow)" stop-opacity="0.95"/>
          <stop offset="0.45" stop-color="var(--globe-violet)" stop-opacity="0.6"/>
          <stop offset="1" stop-color="var(--bg-violet)" stop-opacity="0"/>
        </radialGradient>
      </defs>
      <rect width="260" height="150" fill="url(#globeGlow)"/>
    </svg>

    <div class="brand">
      <span class="brand-mark"></span>
      <span class="brand-name">Varnel Brix</span>
    </div>

    <p class="tagline">11322 Whitepapers from 726 Companies</p>
  </header>
</body>
</html>
```